12 Meter Banner-Design Lagerhalle
Zielgruppe
Wir errichten neue Elektroanlagen für Einfamilenhäuser und Wohnungen.
Hallo,
wir möchten auf 12 Meter drei Banner spannen um die unschönen Rohre und Kabel zu verdecken. Jeder der drei Banner soll 400cm breit und 160cm hoch werden.
-Banner 1 links: Motivationsspruch groß, mittig - : Wer immer tut, was er schon kann, bleibt immer das, was er schon ist.
- Banner 2 mitte : Komfortzone ( Grafiken habe ich im Anhang von dem Aufbau der Komfortzone ) Toll wäre ein selbst erstelltes Design passend zum Unternehmen / Farben Schriftart etc.
-Banner 3 rechts: Motivationsspruch : Zusammenkommen ist ein Beginn, zusammenbleiben ist ein Fortschritt, zusammenarbeiten ist ein Erfolg.
- Design nach Vorgabe Druckpilot ( Datasheet) erstellen
Gundsätzlich wäre super, wenn alle 3 Designs/ Banner miteinander harmonieren. Alles andere ist der Kreativität überlassen.
Schriftart: Fira Sans / Montserrat
Wir würden uns über eine Zusammenarbeit freuen.
Beste Grüße

```html
<!DOCTYPE html>
<html lang="de">
<head>
<meta charset="utf-8">
<title>Banner Komfortzone</title>
<link rel="stylesheet" href="https://fonts.googleapis.com/css2?family=Montserrat:wght@400;700&display=swap">
<style>
  :root {
    --page-bg: #f2f2f3;
    --banner-blue: #1c99cf;
    --zone-growth: #55a6d6;
    --zone-learn: #84b7df;
    --zone-fear: #aacbe8;
    --zone-comfort: #ffffff;
    --text-light: #ffffff;
    --text-blue: #1c99cf;
  }
  html, body {
    margin: 0;
    padding: 0;
    width: 1200px;
    height: 1200px;
    overflow: hidden;
    background: var(--page-bg);
  }
  .canvas {
    position: relative;
    width: 1200px;
    height: 1200px;
    display: flex;
    align-items: center;
    justify-content: center;
  }
  .banner {
    display: block;
    width: 1120px;
    height: 448px;
  }
  .banner text {
    font-family: "Montserrat", sans-serif;
    text-anchor: middle;
    dominant-baseline: central;
  }
  .keyword { font-size: 20px; font-weight: 400; letter-spacing: 0.3px; fill: var(--text-light); }
  .keyword--blue { fill: var(--text-blue); }
  .zone-title { font-size: 24px; font-weight: 700; fill: var(--text-light); text-decoration: underline; }
  .zone-title--blue { fill: var(--text-blue); }
  .vision-label { font-size: 24px; font-weight: 700; fill: var(--text-blue); }
</style>
</head>
<body>
<main class="canvas">
  <svg class="banner" viewBox="0 0 1753 701" xmlns="http://www.w3.org/2000/svg" aria-label="Banner: Von der Komfortzone zur Vision">
    <rect class="banner-bg" width="1753" height="701" fill="var(--banner-blue)"/>

    <ellipse class="zone zone-growth" cx="751" cy="350" rx="683" ry="275" fill="var(--zone-growth)"/>
    <ellipse class="zone zone-learn" cx="614" cy="350" rx="546" ry="210" fill="var(--zone-learn)"/>
    <ellipse class="zone zone-fear" cx="449" cy="350" rx="381" ry="163" fill="var(--zone-fear)"/>
    <ellipse class="zone zone-comfort" cx="312" cy="350" rx="240" ry="120" fill="var(--zone-comfort)"/>

    <g class="keywords-growth">
      <text class="keyword" x="919" y="122">Zielerreichung</text>
      <text class="keyword" x="1176" y="204">Sinnfindung</text>
      <text class="keyword" x="1176" y="490">Selbstsicherheit</text>
      <text class="keyword" x="919" y="568">Zufriedenheit</text>
    </g>
    <g class="keywords-learn">
      <text class="keyword" x="680" y="173">Neue Skills</text>
      <text class="keyword" x="919" y="253">Erfahrungen</text>
      <text class="keyword" x="919" y="457">Selbstvertrauen</text>
      <text class="keyword" x="680" y="522">Zonenausbau</text>
    </g>
    <g class="keywords-fear">
      <text class="keyword" x="462" y="217">Unsicherheit</text>
      <text class="keyword" x="614" y="253">Ablehnung</text>
      <text class="keyword" x="614" y="457">Ausreden</text>
      <text class="keyword" x="462" y="487">Abbruch</text>
    </g>
    <g class="keywords-comfort">
      <text class="keyword keyword--blue" x="205" y="294">Sicherheit</text>
      <text class="keyword keyword--blue" x="414" y="294">Routine</text>
      <text class="keyword keyword--blue" x="206" y="404">Kontrolle</text>
      <text class="keyword keyword--blue" x="413" y="404">Gwohnheit</text>
    </g>

    <g class="zone-titles">
      <text class="zone-title zone-title--blue" x="312" y="348">KOMFORTZONE</text>
      <text class="zone-title" x="690" y="348">ANGSTZONE</text>
      <text class="zone-title" x="986" y="348">LERNZONE</text>
      <text class="zone-title" x="1297" y="348">WACHSTUMSZONE</text>
    </g>

    <g class="arrow" fill="none" stroke="var(--text-light)" stroke-width="6" stroke-linecap="round" stroke-linejoin="round">
      <line x1="1455" y1="350" x2="1491" y2="350"/>
      <polyline points="1478,337 1492,350 1478,363"/>
    </g>

    <circle class="vision" cx="1595" cy="347" r="81" fill="var(--zone-comfort)"/>
    <text class="vision-label" x="1595" y="348">VISION</text>
  </svg>
</main>
</body>
</html>
```